Eneginering consultancy brochure style web design project

Looking for a new brochure style web page for our small engineering consultancy. The prupose of the website is to provide some basic information with about the company, including exampels of our work, and present a way to initiate contact. There there will only be a few pages (up to 5) and limited content.A main focus of the project is to develop the visual design/identity for the webpage, and to provide the template for us to add content, rearrange layout and modify pages with relative ease.A mixture of text and images will be used. The use of an image slider would be desirable.We have recently had a new company logo developed (uploaded), which defines the colour scheme for the page.A professional. clean look is desired, that is not cluttered and easy to navigate.Template to add a photo slider is desirable.The use of swirl patterns (suach as those used here: https://www.brightvortexlab.co.uk/) and/or contoured mesh pattern (example attached) within the page is likely to be attractive, as this is in harmony with our activities.

Target Market(s)

Engineering; manufacturing

Industry/Entity Type

Engineering Consultant

Coding

Coded - Design and coding required

Number of Pages Required

3 page

Font styles to use
Other font styles liked:
• Helvetica

Colors
00a990
33b8a4
86cfc6
606060
3176b5
0255a3
85acd3
474747
7f7f7f

Requirements
Must have
• 1) Landing page for information about the company. Mostly text, with image slider.
• 2) One page for example projects. Images with accompanying texts.
• 3) Enquiry/'get in touch' page.
• Simple, uncluttered look and feel.

```html
<!DOCTYPE html>
<html lang="en">
<head>
<meta charset="utf-8">
<title>Northfield Thermal Systems</title>
<link href="https://fonts.googleapis.com/css2?family=Arimo:wght@400;700&display=swap" rel="stylesheet">
<style>
:root{
  --teal:#00a990;
  --teal-mid:#33b8a4;
  --teal-soft:#86cfc6;
  --teal-pale:#d6efeb;
  --blue:#3176b5;
  --blue-deep:#0255a3;
  --blue-soft:#85acd3;
  --footer-blue:#2c70b8;
  --grey:#606060;
  --grey-dark:#474747;
  --grey-light:#7f7f7f;
  --white:#ffffff;
}
*{margin:0;padding:0;box-sizing:border-box}
html,body{width:1200px;height:2913px;overflow:hidden}
body{font-family:"Arimo",Helvetica,Arial,sans-serif;color:var(--grey);background:var(--white);position:relative}
h1,h2,h3,h4{font-weight:400}
.abs{position:absolute}
.btn{position:absolute;display:flex;align-items:center;justify-content:center;font-size:13px;color:var(--white);background:var(--blue);border:1px solid var(--blue-deep)}
.btn--light{background:var(--white);color:var(--blue);border:none}

/* header */
.site-header{left:0;top:0;width:1200px;height:80px;background:rgba(255,255,255,.92);z-index:2}
.brand{left:120px;top:22px;display:flex;align-items:center;gap:10px;font-size:22px;font-weight:700;color:var(--blue-deep)}
.brand-mark{width:14px;height:14px;background:var(--teal)}
.nav{top:31px;font-size:13px;color:var(--blue-deep)}
.nav-call span{color:var(--teal)}

/* hero */
.hero{left:0;top:0;width:1200px;height:600px;background:radial-gradient(ellipse at 30% 30%,#5fb0e8 0%,#2f8fd8 35%,#2064c4 70%,#2a7fd0 100%)}
.hero-title{left:0;top:270px;width:1200px;text-align:center;font-size:38px;line-height:46px;color:var(--white)}
.hero .btn{left:519px;top:393px;width:161px;height:40px}

/* about */
.about-bar{left:178px;top:680px;width:3px;height:72px;background:var(--teal)}
.about-title{left:240px;top:683px;font-size:29px;line-height:36px;color:var(--blue)}
.about-text{left:660px;top:678px;width:300px;font-size:13.5px;line-height:19.5px;text-align:justify;color:var(--grey)}
.about-text p+p{margin-top:20px}

/* services tabs */
.tab{left:0;width:420px;height:120px;padding:38px 0 0 120px;font-size:20px;line-height:26px}
.tab-num{position:absolute;left:122px;top:-10px;width:20px;height:20px;border-radius:50%;background:var(--white);font-size:10px;display:flex;align-items:center;justify-content:center;color:var(--grey)}
.tab--1{top:1080px;background:var(--teal-pale);color:var(--grey-dark)}
.tab--2{top:1200px;background:var(--blue);color:var(--white);font-weight:700}
.tab--2 .tab-num{background:var(--teal-mid);color:var(--white)}
.tab--3{top:1320px;background:#b8e3dd;color:var(--grey-dark)}
.tab--4{top:1440px;background:#a3d9d0;color:var(--grey)}
.service-visual{left:420px;top:1080px;width:780px;height:480px;background:linear-gradient(160deg,#6a6a6a 0%,#2c2c2c 45%,#4a2a22 75%,#2a4a55 100%)}
.tab-arrow{left:420px;top:1200px}
.service-title{left:540px;top:1283px;font-size:28px;line-height:34px;color:var(--white);font-weight:700}
.service-text{left:540px;top:1365px;width:520px;font-size:13px;line-height:19px;color:var(--white)}
.service-visual-btn{left:540px;top:1482px;width:128px;height:40px}

/* contact */
.frame-back{left:258px;top:1643px;width:358px;height:455px;border:8px solid #e6e9ec}
.frame{left:240px;top:1625px;width:358px;height:455px;border:8px solid var(--teal-mid);background:var(--white)}
.field{left:300px;width:240px;border-bottom:1px solid #d5dadc}
.field-label{font-size:12px;color:var(--teal)}
.field-value{font-size:18px;color:var(--grey-dark);margin-top:6px}
.contact-title{left:600px;top:1715px;font-size:28px;line-height:36px;color:var(--blue)}
.contact-rule{left:592px;top:1830px;width:368px;height:7px;background:var(--teal-mid)}
.contact-email{left:660px;top:1916px;font-size:13px;color:var(--grey)}
.contact-phone{left:660px;top:1938px;font-size:20px;color:var(--teal)}
.contact-phone b{font-weight:400;color:var(--grey)}

/* software */
.software{left:0;top:2160px;width:1200px;height:375px;background:var(--teal-pale)}
.software-title{left:0;top:2237px;width:1200px;text-align:center;font-size:28px;color:var(--blue)}
.software-sub{left:0;top:2277px;width:1200px;text-align:center;font-size:13px;line-height:21px;color:var(--grey)}
.vendor{top:2385px;height:70px;font-size:24px;color:var(--grey-dark);display:flex;align-items:center;justify-content:center;gap:8px;white-space:nowrap}
.vendor i{display:block;width:14px;height:14px;background:var(--blue);flex:none}

/* footer */
.site-footer{left:0;top:2535px;width:1200px;height:378px;background:var(--footer-blue)}
.foot-col{top:2615px;font-size:12px;line-height:19px;color:var(--white)}
.foot-col h4{font-size:14px;font-weight:700;margin-bottom:18px}
.foot-col h4.foot-copy{font-size:13px;font-weight:400;margin-bottom:4px}
.foot-call{font-size:20px;margin-top:4px}
.to-top{left:1127px;top:2617px;width:24px;height:24px;border-radius:50%;background:var(--teal-mid)}
</style>
</head>
<body>

<section class="hero abs" role="img" aria-label="Colour-mapped CFD mesh of a fan blade in blues and greens">
  <h1 class="hero-title abs">Thermal Design, Simulations and<br>Analysis of Electrical Machines</h1>
  <div class="btn btn--light">Explore More</div>
</section>

<header class="site-header abs">
  <div class="brand abs"><span class="brand-mark"></span>Northfield Thermal</div>
  <div class="nav abs" style="left:545px">Home</div>
  <div class="nav abs" style="left:625px">About Us</div>
  <div class="nav abs" style="left:726px">Services</div>
  <div class="nav abs" style="left:822px">Contact</div>
  <div class="nav nav-call abs" style="left:913px">Call: <span>+44 (0)7700 900 314</span></div>
</header>

<section class="about">
  <div class="about-bar abs"></div>
  <h2 class="about-title abs">About Northfield Thermal<br>Systems</h2>
  <div class="about-text abs">
    <p>NTS is a thermal engineering consultancy, specialising in the thermal design, simulation and analysis of electrical machines. Our experience spans across traditional and novel machine arrangements, with extensive experience with Permanent Magnet, Induction, Synchronous, Switched Reluctance and Synchronous Reluctance machines.</p>
    <p>Machines have been designed to operate in a range of applications and environments including automotive, aerospace, marine, energy generation and energy recovery.</p>
  </div>
  <div class="btn" style="left:660px;top:960px;width:128px;height:40px">Explore More</div>
</section>

<section class="services">
  <div class="service-visual abs" role="img" aria-label="Rendered gearbox assembly with translucent housing and gears"></div>
  <svg class="tab-arrow abs" width="58" height="120" viewBox="0 0 58 120"><polygon points="0,0 58,60 0,120" fill="#3176b5"/></svg>
  <div class="tab tab--1 abs"><span class="tab-num">1</span>Thermal Analysis<br>and Design</div>
  <div class="tab tab--2 abs"><span class="tab-num">2</span>Thermo-fluid Modelling<br>and Simulation</div>
  <div class="tab tab--3 abs"><span class="tab-num">3</span>Thermal Simulation<br>Tools</div>
  <div class="tab tab--4 abs"><span class="tab-num">4</span>Test Data<br>Acquisition</div>
  <h3 class="service-title abs">Thermo-fluid modelling and<br>simulation</h3>
  <p class="service-text abs">Lorem ipsum dolor sit amet, consectetur adipiscing elit, sed do eiusmod tempor incididunt ut labore et dolore magna aliqua. Ut enim ad minim veniam, quis nostrud exercitation ullamco laboris nisi ut aliquip ex ea.</p>
  <div class="btn btn--light service-visual-btn">Learn More</div>
</section>

<section class="contact">
  <div class="frame-back abs"></div>
  <div class="frame abs"></div>
  <div class="field abs" style="top:1712px;height:66px"><div class="field-label">Name</div><div class="field-value">Lorem Ipsum</div></div>
  <div class="field abs" style="top:1793px;height:66px"><div class="field-label">Email</div></div>
  <div class="field abs" style="top:1873px;height:105px"><div class="field-label">Message ...</div></div>
  <div class="btn" style="left:300px;top:2000px;width:95px;height:40px">Send</div>
  <h2 class="contact-title abs">Contact Us Today!<br>for a Free Consultation</h2>
  <div class="contact-rule abs"></div>
  <div class="contact-email abs">e. enquiries@northfieldthermal.co.uk</div>
  <div class="contact-phone abs"><b>P.</b> +44 (0)7700 900 314</div>
  <div class="btn" style="left:660px;top:2000px;width:128px;height:40px">Contact Us</div>
</section>

<section class="software abs"></section>
<h2 class="software-title abs">Software</h2>
<p class="software-sub abs">We are experienced with many different software packages, enabling us to<br>select the most appropriate tools for each project.</p>
<div class="vendor abs" style="left:200px;width:270px"><i></i>FlowCore</div>
<div class="vendor abs" style="left:485px;width:140px"><i></i>MathGrid</div>
<div class="vendor abs" style="left:640px;width:175px"><i></i>SimPhase</div>
<div class="vendor abs" style="left:835px;width:185px"><i></i>Rotor Lab</div>

<footer class="site-footer abs"></footer>
<div class="foot-col abs" style="left:120px">
  <h4 class="foot-copy">Copyright © 2019</h4>
  Northfield Thermal Systems Ltd.<br>All rights reserved.
  <svg style="display:block;margin-top:20px" width="80" height="14" viewBox="0 0 80 14">
    <rect x="1" y="1" width="12" height="12" fill="none" stroke="#fff"/>
    <circle cx="31" cy="7" r="6" fill="none" stroke="#fff"/>
    <rect x="49" y="1" width="12" height="12" fill="none" stroke="#fff"/>
  </svg>
</div>
<div class="foot-col abs" style="left:360px">
  <h4>Northfield Thermal Systems Ltd</h4>
  Aldgate House<br>Riverside Innovation Park<br>Kestrel Road<br>Derby<br>DE1 4QX
</div>
<div class="foot-col abs" style="left:730px">
  <h4>Contact Us</h4>
  e. enquiries@northfieldthermal.co.uk
  <div class="foot-call">Call: +44 (0)7700 900 314</div>
</div>
<div class="to-top abs"><svg width="24" height="24" viewBox="0 0 24 24"><polyline points="8,14 12,10 16,14" fill="none" stroke="#fff" stroke-width="2"/></svg></div>

</body>
</html>
```